Advertisement flyer for fire sprinkler repair parts. The projected audience are contractors.

I need a flyer advertising specific parts that we are stocking at our company "Meridian Valvecraft Supply." I have attached a picture of our logo. I want the title to say "Fire Pump Repair Parts and Accessories." I want to specifically advertise the following parts: Repack Kits and Repair Parts, Jockey Pumps, Pump Controllers, Casing Relief Valves, Air Release Valves, Suction/Discharge Gauges, Pump Shaft Couplers & Shim Kits, Fire Pump Relief Valves, and QN Listed Pressure Reducing Valves. I have attached pictures of the manufacturers I want to advertise on this flyer. I have also attached pictures of some of the parts we are stocking that I would like to be included somewhere in the flyer. I would like all of the pictures to have a transparent background. Also I would like our phone number :(800)-431-2867, and our website www.tolvenspares.example included. I made my own design that I have Attached. You do not have to go based off this design, but I would like the basic content to be the same. We do have Same- Day shipping as well as Free Tech Support if you can include that anywhere.

```html
<!DOCTYPE html>
<html lang="en">
<head>
<meta charset="utf-8">
<title>Fire Pump Repair Parts &amp; Accessories</title>
<link rel="stylesheet" href="https://fonts.googleapis.com/css2?family=Bebas+Neue&family=Open+Sans:ital,wght@0,600;0,700;1,800&display=swap">
<style>
  :root {
    --page-bg: #e4e5e7;
    --brand-red: #e8302f;
    --deep-red: #b3171a;
    --title-yellow: #f5ec1a;
    --call-orange: #f7a21c;
    --ink: #1c1c1c;
    --white: #ffffff;
    --tick-green: #1f9a3a;
    --label-light: #ffffff;
    --label-shade: #d6d6d6;
    --footer-line: #c9c9cb;
  }
  * { box-sizing: border-box; margin: 0; padding: 0; }
  html, body { width: 1200px; height: 1200px; overflow: hidden; background: var(--page-bg); }
  .flyer {
    position: absolute; left: 144px; top: 10px;
    width: 876px; height: 1134px;
    transform: scale(1.04); transform-origin: top left;
    background: var(--white); overflow: hidden;
    font-family: "Bebas Neue", "Oswald", sans-serif;
  }
  .hero {
    position: absolute; left: 0; top: 0; width: 876px; height: 268px;
    background:
      linear-gradient(180deg, rgba(150,10,15,.35), rgba(200,30,35,.15)),
      linear-gradient(100deg, #c81b21 0%, #e9494a 35%, #d92a2e 65%, #a5121a 100%);
  }
  .hero-title { position: absolute; left: 0; width: 876px; text-align: center; line-height: 1; }
  .hero-title .line-one { position: absolute; left: 0; top: 58px; width: 876px; color: var(--white); font-size: 100px; letter-spacing: 1px; }
  .hero-title .line-two { position: absolute; left: 0; top: 148px; width: 876px; color: var(--title-yellow); font-size: 86px; letter-spacing: 1px; }
  .red-panel { position: absolute; left: 0; top: 266px; }
  .product-shot { position: absolute; }
  .shot-fire-pumps { left: 60px; top: 288px; width: 310px; height: 200px; border-radius: 40px 40px 10px 10px;
    background: radial-gradient(ellipse at 50% 55%, #d8262b 0%, #c41f24 45%, rgba(255,255,255,0) 72%); }
  .shot-jockey-pump { left: 118px; top: 508px; width: 70px; height: 206px; border-radius: 12px;
    background: linear-gradient(180deg, #efe2c4 0%, #e2cfa3 22%, #2f6db5 30%, #c9cdd3 50%, #9ea4ac 75%, #2f6db5 100%); }
  .shot-reducing-valve { left: 278px; top: 512px; width: 100px; height: 210px; border-radius: 18px;
    background: linear-gradient(180deg, #c92a2a 0%, #b08c4c 18%, #8e6c33 60%, #a98347 100%); }
  .shot-repack-kit { left: 0; top: 748px; width: 437px; height: 292px;
    background: radial-gradient(ellipse at 50% 50%, #b9a58a 0%, #a9a6a3 55%, #a2a2a2 100%); }
  .parts-list { position: absolute; left: 420px; top: 302px; list-style: none; }
  .parts-list li { position: relative; height: 41.3px; }
  .tick-box { position: absolute; left: 0; top: 0; width: 40px; height: 38px; }
  .part-label {
    position: absolute; left: 50px; top: 1px; height: 36px;
    padding-left: 10px; font-size: 29px; line-height: 38px; color: var(--ink);
    background: linear-gradient(180deg, var(--label-light) 0%, #f2f2f2 60%, var(--label-shade) 100%);
    clip-path: polygon(0 0, 100% 0, calc(100% - 28px) 100%, 0 100%);
    box-shadow: 0 2px 3px rgba(0,0,0,.3);
  }
  .call-cta { position: absolute; left: 500px; top: 780px; color: var(--call-orange); font-size: 44px; line-height: 1; }
  .phone { position: absolute; left: 500px; top: 828px; color: var(--white); font-size: 66px; line-height: 1; letter-spacing: 1px; }
  .web-button {
    position: absolute; left: 480px; top: 918px; width: 356px; height: 58px; border-radius: 14px;
    background: linear-gradient(180deg, #ff6a3a 0%, #e8302f 55%, #c2181c 100%);
    box-shadow: 0 6px 8px rgba(0,0,0,.35);
    font-family: "Open Sans", Arial, sans-serif; font-style: italic; font-weight: 800;
    font-size: 22px; color: var(--title-yellow); text-align: center; line-height: 56px;
  }
  .maker-strip {
    position: absolute; left: 0; top: 1040px; width: 876px; height: 94px;
    border-top: 10px solid var(--footer-line); background: var(--white);
    display: flex; align-items: center; justify-content: space-around; padding: 0 24px;
  }
  .maker { font-family: "Open Sans", Arial, sans-serif; font-weight: 700; font-size: 11.5px; color: #2a4d8f; display: flex; align-items: center; gap: 4px; white-space: nowrap; }
  .maker .mark { width: 8px; height: 8px; background: currentColor; }
  .maker.red { color: #c41f24; }
  .maker.dark { color: #1c1c1c; }
</style>
</head>
<body>
<main class="flyer">
  <div class="hero" role="img" aria-label="Red-tinted fire pump room with piping and valves"></div>
  <h1 class="hero-title">
    <span class="line-one">FIRE PUMP REPAIR</span>
    <span class="line-two">PARTS &amp; ACCESSORIES!</span>
  </h1>

  <svg class="red-panel" width="876" height="774" viewBox="0 266 876 774" aria-hidden="true">
    <path d="M369 268 Q430 272 437 332 L437 1040 L876 1040 L876 268 Z" fill="var(--brand-red)"/>
  </svg>

  <div class="product-shot shot-fire-pumps" role="img" aria-label="Horizontal split-case and vertical inline fire pumps"></div>
  <div class="product-shot shot-jockey-pump" role="img" aria-label="Vertical multistage jockey pump"></div>
  <div class="product-shot shot-reducing-valve" role="img" aria-label="Bronze pressure reducing valve"></div>
  <div class="product-shot shot-repack-kit" role="img" aria-label="Fire pump repack kit with gaskets, packing rings and bolts"></div>

  <ul class="parts-list">
    <li><svg class="tick-box" viewBox="0 0 40 38"><rect x="1" y="1" width="38" height="36" fill="#fff" stroke="#222" stroke-width="2"/><path d="M7 20 L16 29 L35 6" fill="none" stroke="var(--tick-green)" stroke-width="5"/></svg><span class="part-label" style="width:244px">FIRE PUMP REPACK KITS</span></li>
    <li><svg class="tick-box" viewBox="0 0 40 38"><rect x="1" y="1" width="38" height="36" fill="#fff" stroke="#222" stroke-width="2"/><path d="M7 20 L16 29 L35 6" fill="none" stroke="var(--tick-green)" stroke-width="5"/></svg><span class="part-label" style="width:174px">JOCKEY PUMPS</span></li>
    <li><svg class="tick-box" viewBox="0 0 40 38"><rect x="1" y="1" width="38" height="36" fill="#fff" stroke="#222" stroke-width="2"/><path d="M7 20 L16 29 L35 6" fill="none" stroke="var(--tick-green)" stroke-width="5"/></svg><span class="part-label" style="width:214px">PUMP CONTROLLERS</span></li>
    <li><svg class="tick-box" viewBox="0 0 40 38"><rect x="1" y="1" width="38" height="36" fill="#fff" stroke="#222" stroke-width="2"/><path d="M7 20 L16 29 L35 6" fill="none" stroke="var(--tick-green)" stroke-width="5"/></svg><span class="part-label" style="width:234px">CASING RELIEF VALVES</span></li>
    <li><svg class="tick-box" viewBox="0 0 40 38"><rect x="1" y="1" width="38" height="36" fill="#fff" stroke="#222" stroke-width="2"/><path d="M7 20 L16 29 L35 6" fill="none" stroke="var(--tick-green)" stroke-width="5"/></svg><span class="part-label" style="width:219px">AIR RELEASE VALVES</span></li>
    <li><svg class="tick-box" viewBox="0 0 40 38"><rect x="1" y="1" width="38" height="36" fill="#fff" stroke="#222" stroke-width="2"/><path d="M7 20 L16 29 L35 6" fill="none" stroke="var(--tick-green)" stroke-width="5"/></svg><span class="part-label" style="width:299px">SUCTION / DISCHARGE GAUGES</span></li>
    <li><svg class="tick-box" viewBox="0 0 40 38"><rect x="1" y="1" width="38" height="36" fill="#fff" stroke="#222" stroke-width="2"/><path d="M7 20 L16 29 L35 6" fill="none" stroke="var(--tick-green)" stroke-width="5"/></svg><span class="part-label" style="width:164px">FLOW METERS</span></li>
    <li><svg class="tick-box" viewBox="0 0 40 38"><rect x="1" y="1" width="38" height="36" fill="#fff" stroke="#222" stroke-width="2"/><path d="M7 20 L16 29 L35 6" fill="none" stroke="var(--tick-green)" stroke-width="5"/></svg><span class="part-label" style="width:344px">PUMP SHAFT COUPLERS &amp; SHIM KITS</span></li>
    <li><svg class="tick-box" viewBox="0 0 40 38"><rect x="1" y="1" width="38" height="36" fill="#fff" stroke="#222" stroke-width="2"/><path d="M7 20 L16 29 L35 6" fill="none" stroke="var(--tick-green)" stroke-width="5"/></svg><span class="part-label" style="width:259px">FIRE PUMP RELIEF VALVES</span></li>
    <li><svg class="tick-box" viewBox="0 0 40 38"><rect x="1" y="1" width="38" height="36" fill="#fff" stroke="#222" stroke-width="2"/><path d="M7 20 L16 29 L35 6" fill="none" stroke="var(--tick-green)" stroke-width="5"/></svg><span class="part-label" style="width:374px">QN LISTED PRESSURE REDUCING VALVES</span></li>
  </ul>

  <p class="call-cta">CALL US TODAY</p>
  <p class="phone">(800) 431-2867</p>
  <p class="web-button">www.tolvenspares.example</p>

  <footer class="maker-strip">
    <span class="maker red"><span class="mark"></span>Meridian Valvecraft Supply</span>
    <span class="maker dark">Corvane Pump</span>
    <span class="maker">Halvorn Pump</span>
    <span class="maker">Ostrel</span>
    <span class="maker">Brisca</span>
    <span class="maker">Kestrum</span>
    <span class="maker">Wendale Marsh</span>
    <span class="maker red">Tarrow Pump</span>
    <span class="maker dark">Ferrox</span>
  </footer>
</main>
</body>
</html>
```